Medical Cannabis company is looking for a LOGO design *

SILVER MERIDIAN (SM) is a new company in the Israeli medical cannabis industry. We will engage in PREMIUM medical cannabis growing and cultivation and also manufacturing of HIGH-END cannabis based medical products.
the design should reflect luxury, high-end and Pharma-grade products.
the design should use color GOLD and NOT using the famous cannabis leaf !

Target Market(s)

international medical cannabis Pharmaceutical companies
and of course local and international patients

Contact Information for Business Card

Ron Ben-Amit
Founder and CEO

Silver Meridian
Medical grade cannabis

ronbenamit@mailpost-example.com
972-52-3186407

Colors
ffc214
fbed22

Requirements
Must have
• clean and simple
• luxury
• gold !!
• (can also have green for Cannabis and/or blue for Pharma)
Should not have
• cannabis leaf

```html
<!DOCTYPE html>
<html lang="en">
<head>
<meta charset="utf-8">
<title>Silver Meridian – Business Card</title>
<link href="https://fonts.googleapis.com/css2?family=Cinzel:wght@400&family=Lato:wght@400;700&display=swap" rel="stylesheet">
<style>
  :root {
    --navy: #030716;
    --yellow: #fbed22;
    --gold: #ffc214;
    --silver: #d9d9de;
    --backdrop: #ecebe8;
  }
  html, body {
    margin: 0;
    width: 1200px;
    height: 900px;
    overflow: hidden;
    background: var(--backdrop);
  }
  .business-card {
    position: absolute;
    left: 120px;
    top: 152px;
    width: 960px;
    height: 596px;
    background: var(--navy);
    box-shadow: 0 14px 40px rgba(0,0,0,0.18);
    overflow: hidden;
  }
  .card-waves {
    position: absolute;
    inset: 0;
    width: 100%;
    height: 100%;
  }
  .brand {
    position: absolute;
    right: 66px;
    top: 218px;
    text-align: center;
  }
  .brand-name {
    font-family: 'Lato', sans-serif;
    font-weight: 700;
    font-size: 46px;
    line-height: 1;
    color: var(--yellow);
    letter-spacing: -0.5px;
  }
  .brand-tagline {
    margin-top: 8px;
    font-family: 'Cinzel', serif;
    font-size: 20px;
    letter-spacing: 3px;
    color: var(--silver);
  }
  .contact {
    position: absolute;
    left: 41px;
    top: 362px;
    color: var(--navy);
  }
  .person-name {
    font-family: 'Cinzel', serif;
    font-size: 33px;
    letter-spacing: 1px;
    line-height: 1.1;
  }
  .person-title {
    margin-top: 8px;
    font-family: 'Lato', sans-serif;
    font-size: 21px;
    line-height: 1.2;
  }
  .contact-lines {
    margin-top: 38px;
    font-family: 'Lato', sans-serif;
    font-size: 22px;
  }
  .contact-line {
    display: flex;
    align-items: center;
    gap: 10px;
    height: 38px;
  }
  .contact-icon {
    width: 20px;
    height: 20px;
    fill: var(--navy);
  }
</style>
</head>
<body>
  <div class="business-card">
    <svg class="card-waves" viewBox="0 0 652 404" preserveAspectRatio="none" aria-hidden="true">
      <path d="M0,62 C160,185 360,268 600,292" fill="none" stroke="var(--yellow)" stroke-width="3"/>
      <path d="M0,78 C170,205 380,290 652,296 L652,404 L0,404 Z" fill="var(--yellow)"/>
      <path d="M0,73 C165,196 370,278 590,296" fill="none" stroke="var(--navy)" stroke-width="4"/>
    </svg>

    <div class="brand">
      <div class="brand-name">Silver Meridian</div>
      <div class="brand-tagline">MEDICAL GRADE CANNABIS</div>
    </div>

    <div class="contact">
      <div class="person-name">RON BEN-AMIT</div>
      <div class="person-title">FOUNDER AND CEO</div>
      <div class="contact-lines">
        <div class="contact-line">
          <svg class="contact-icon" viewBox="0 0 24 24" aria-hidden="true"><path d="M6.6 10.8a15.1 15.1 0 0 0 6.6 6.6l2.2-2.2c.3-.3.7-.4 1-.2 1.1.4 2.3.6 3.6.6.6 0 1 .4 1 1V20c0 .6-.4 1-1 1C10.6 21 3 13.4 3 4c0-.6.4-1 1-1h3.5c.6 0 1 .4 1 1 0 1.3.2 2.5.6 3.6.1.3 0 .7-.2 1z"/></svg>
          <span>972-52-3186407</span>
        </div>
        <div class="contact-line">
          <svg class="contact-icon" viewBox="0 0 24 24" aria-hidden="true"><path d="M3 5h18v14H3z M3 5l9 7 9-7" fill="var(--navy)"/><path d="M3.5 6l8.5 6.5L20.5 6" fill="none" stroke="var(--yellow)" stroke-width="1.6"/></svg>
          <span>RONBENAMIT@MAILPOST-EXAMPLE.COM</span>
        </div>
      </div>
    </div>
  </div>
</body>
</html>
```